Web Design for an Innovative Life Science Marketplace

IMPORTANT:
The software is called CS-Cart. It has capabilities and limitations with design features in the software. There is a certain framework that needs to be followed. It is PHP and Linux. It may require add-ons for your design, so please be specific with what is required. It’s preferred the designer has CS-Cart knowledge/experience.

Key Requirements
1. I’d like the design to include an implemented/recommended CS-Cart theme that is consistent with our branding (see the marketing collateral and logo).
2. I then need the additional design changes to that theme to create the below web pages.
3. All designs should be consistent with our branding. All pictures should either be computer generated (clip art-like) or pictures of happy patients. What is a happy patient? Close up photo of someone healthy, happy, and experiencing/enjoying life. Not someone in a hospital or getting care. Please see examples already on the site.

Please see the attached Web Design details in the word document. That document is important to complete the design.

```html
<!DOCTYPE html>
<html lang="en">
<head>
<meta charset="utf-8">
<title>VerdaLink – Join the Circular Supply Chain</title>
<link href="https://fonts.googleapis.com/css2?family=Open+Sans:wght@400;600;700&family=Montserrat:wght@500;600;700&display=swap" rel="stylesheet">
<style>
:root{
  --green:#8cc63f;
  --green-dark:#6fa82b;
  --green-light:#d9ecbf;
  --teal:#2f8f8c;
  --ink:#333;
  --muted:#777;
  --line:#e3e3e3;
  --footer:#2b2b2b;
  --footer-bar:#1f1f1f;
  --white:#fff;
}
*{box-sizing:border-box;margin:0;padding:0}
html,body{width:1200px;height:2316px;overflow:hidden;background:var(--white)}
body{font-family:"Open Sans",Arial,sans-serif;color:var(--ink);position:relative}
h1,h2,h3,h4{font-family:"Montserrat",Arial,sans-serif}

.site-header{position:absolute;top:0;left:0;width:1200px;height:60px;background:var(--white);border-bottom:1px solid var(--line)}
.brand{position:absolute;left:40px;top:14px;display:flex;align-items:center;gap:10px}
.brand-mark{width:30px;height:30px;background:var(--green);border-radius:4px}
.brand-name{font-family:"Montserrat",Arial,sans-serif;font-weight:700;font-size:22px;color:var(--teal);letter-spacing:.5px}
.search{position:absolute;left:480px;top:6px;width:300px;height:20px;border:1px solid #ccc;border-radius:2px;font-size:10px;color:#aaa;padding:3px 8px}
.search svg{position:absolute;right:6px;top:4px}
.account-links{position:absolute;right:40px;top:9px;font-size:10px;color:var(--muted);display:flex;gap:16px}
.main-nav{position:absolute;left:470px;top:36px;display:flex;gap:24px;font-size:11px;color:#555}
.main-nav a{color:inherit;text-decoration:none}
.main-nav .active{color:var(--green-dark);font-weight:600}

.hero{position:absolute;top:60px;left:0;width:1200px;height:600px;background:linear-gradient(100deg,#3f6b2d 0%,#7fae4a 40%,#b9d68c 70%,#e7eed9 100%)}
.hero-text{position:absolute;left:60px;top:190px;width:420px;color:var(--white)}
.hero-text h1{font-size:40px;font-weight:700;line-height:1.15;margin-bottom:14px}
.hero-text p{font-size:14px;line-height:1.5;margin-bottom:32px}
.btn{display:inline-block;background:var(--green);color:var(--white);font-weight:700;font-size:12px;letter-spacing:1px;padding:12px 40px;border-radius:2px;text-decoration:none}

.section-title{text-align:center;font-size:30px;font-weight:600;color:var(--ink)}
.join{position:absolute;top:660px;left:0;width:1200px;height:360px}
.join .section-title{margin-top:76px}
.join-list{display:flex;justify-content:center;gap:110px;margin-top:50px}
.join-item{width:220px;text-align:center}
.join-icon{width:76px;height:76px;border-radius:50%;border:2px solid var(--line);margin:0 auto 18px;display:flex;align-items:center;justify-content:center}
.join-item h3{font-size:15px;font-weight:600;margin-bottom:8px}
.join-item p{font-size:11px;color:var(--muted);line-height:1.5}

.products{position:absolute;top:1020px;left:0;width:1200px;height:460px;display:flex}
.products-art{width:600px;height:460px;position:relative;background:linear-gradient(135deg,#f2a23a 0%,#e9574b 35%,#3aa7b8 70%,#f6d24a 100%)}
.products-label{position:absolute;left:0;top:190px;width:600px;height:56px;background:var(--green-light);display:flex;align-items:center;justify-content:center;font-family:"Montserrat",Arial,sans-serif;font-size:24px;font-weight:600;color:var(--green-dark)}
.products-list{width:600px;height:460px;background:var(--green);padding:60px 80px 0 70px;color:var(--white)}
.product-item{display:flex;gap:14px;margin-bottom:38px}
.product-item h4{font-size:14px;font-weight:600;margin-bottom:4px}
.product-item p{font-size:11px;line-height:1.5;opacity:.95}

.marketing{position:absolute;top:1480px;left:0;width:1200px;height:430px}
.marketing .section-title{margin-top:30px}
.cards{display:flex;justify-content:center;gap:30px;margin-top:36px}
.card{width:400px;height:210px;background:var(--white);box-shadow:0 2px 10px rgba(0,0,0,.15);border-top:3px solid var(--green);padding:34px 40px}
.card h3{font-size:20px;font-weight:500;margin-bottom:10px}
.card p{font-size:11px;color:var(--muted);line-height:1.5;margin-bottom:24px}
.card .btn{font-size:11px;padding:9px 22px}

.promise{position:absolute;top:1910px;left:0;width:1200px;height:210px;background:var(--teal);color:var(--white);display:flex;align-items:center;padding-left:80px}
.promise-head{display:flex;align-items:center;gap:14px;width:420px}
.promise-head h2{font-size:30px;font-weight:500}
.promise blockquote{font-family:"Montserrat",Arial,sans-serif;font-style:italic;font-size:22px;line-height:1.4;width:620px;text-align:center}

.site-footer{position:absolute;top:2120px;left:0;width:1200px;height:160px;background:var(--footer);color:#bbb;font-size:11px;padding:30px 0 0 40px;display:flex;gap:60px}
.site-footer h4{font-size:11px;color:var(--white);font-weight:600;margin-bottom:10px;letter-spacing:.5px}
.site-footer ul{list-style:none;line-height:1.9}
.footer-cols{display:flex;gap:40px}
.contact{margin-left:60px}
.contact-grid{display:grid;grid-template-columns:190px 190px;line-height:1.9}
.footer-bar{position:absolute;top:2280px;left:0;width:1200px;height:36px;background:var(--footer-bar);color:#888;font-size:10px;padding:12px 40px;display:flex;justify-content:space-between}
.social{display:flex;gap:10px}
.social span{width:12px;height:12px;border-radius:50%;background:#777;display:block}
</style>
</head>
<body>

<header class="site-header">
  <div class="brand"><span class="brand-mark"></span><span class="brand-name">VerdaLink</span></div>
  <div class="search">Search
    <svg width="10" height="10" viewBox="0 0 10 10"><circle cx="4" cy="4" r="3" fill="none" stroke="#999" stroke-width="1.2"/><line x1="6.3" y1="6.3" x2="9.5" y2="9.5" stroke="#999" stroke-width="1.2"/></svg>
  </div>
  <div class="account-links"><span>LOG IN</span><span>REGISTER</span></div>
  <nav class="main-nav">
    <a class="active">Home</a><a>Why VerdaLink</a><a>About Us</a><a>Our Partners</a><a>White Paper</a><a>Quality Policy</a>
  </nav>
</header>

<section class="hero" role="img" aria-label="Close-up photo of a smiling, healthy young woman outdoors against green foliage">
  <div class="hero-text">
    <h1>Join the Circular Supply Chain</h1>
    <p>An online marketplace where the life sciences community can connect, share surplus materials and build a greener, more efficient future together.</p>
    <a class="btn">PRE REGISTER</a>
  </div>
</section>

<section class="join">
  <h2 class="section-title">Who Should Join</h2>
  <div class="join-list">
    <div class="join-item">
      <div class="join-icon"><svg width="40" height="36" viewBox="0 0 40 36"><path d="M2 34V16l10 6V16l10 6V6h6v28z" fill="none" stroke="#6fa82b" stroke-width="2"/><line x1="2" y1="34" x2="38" y2="34" stroke="#6fa82b" stroke-width="2"/><rect x="30" y="2" width="6" height="32" fill="none" stroke="#6fa82b" stroke-width="2"/></svg></div>
      <h3>Manufacturers</h3>
      <p>Create an account in minutes to sell or buy excess and obsolete materials and equipment</p>
    </div>
    <div class="join-item">
      <div class="join-icon"><svg width="36" height="36" viewBox="0 0 36 36"><circle cx="15" cy="15" r="10" fill="none" stroke="#6fa82b" stroke-width="2.5"/><line x1="22" y1="22" x2="33" y2="33" stroke="#6fa82b" stroke-width="3"/></svg></div>
      <h3>Researchers</h3>
      <p>Sell or buy low-cost materials and receive donations</p>
    </div>
    <div class="join-item">
      <div class="join-icon"><svg width="36" height="36" viewBox="0 0 36 36"><path d="M4 12h28l-3 20H7z" fill="none" stroke="#6fa82b" stroke-width="2"/><path d="M12 12a6 6 0 0 1 12 0" fill="none" stroke="#6fa82b" stroke-width="2"/></svg></div>
      <h3>Original Suppliers</h3>
      <p>Market your products across a broad life science network</p>
    </div>
  </div>
</section>

<section class="products">
  <div class="products-art" role="img" aria-label="Flat colourful illustration of lab tools, a clock, a phone, scales and equipment">
    <div class="products-label">Products</div>
  </div>
  <div class="products-list">
    <div class="product-item">
      <svg width="16" height="16" viewBox="0 0 16 16"><path d="M2 8l4 4 8-9" fill="none" stroke="#fff" stroke-width="2"/></svg>
      <div><h4>Raw Materials</h4><p>Consumables and starting materials for lab and intermediate manufacturing or research</p></div>
    </div>
    <div class="product-item">
      <svg width="16" height="16" viewBox="0 0 16 16"><path d="M2 8l4 4 8-9" fill="none" stroke="#fff" stroke-width="2"/></svg>
      <div><h4>Equipment</h4><p>Find idle systems decommissioned by labs or manufacturers</p></div>
    </div>
    <div class="product-item">
      <svg width="16" height="16" viewBox="0 0 16 16"><path d="M2 8l4 4 8-9" fill="none" stroke="#fff" stroke-width="2"/></svg>
      <div><h4>Tools</h4><p>Components of a broader system used in an application</p></div>
    </div>
    <div class="product-item">
      <svg width="16" height="16" viewBox="0 0 16 16"><path d="M2 8l4 4 8-9" fill="none" stroke="#fff" stroke-width="2"/></svg>
      <div><h4>Collaborative Relationships</h4><p>Safety stock agreements, advertising, shared testing capacity and supplier audits</p></div>
    </div>
  </div>
</section>

<section class="marketing">
  <h2 class="section-title">Marketing Materials</h2>
  <div class="cards">
    <div class="card">
      <h3>READ OUR WHITE PAPER</h3>
      <p>Learn how a shared marketplace reduces waste and cost, and why a circular supply chain benefits every partner.</p>
      <a class="btn">DOWNLOAD WHITEPAPER</a>
    </div>
    <div class="card">
      <h3>READ OUR BROCHURE</h3>
      <p>A short overview of our platform, the members we serve and the products you can trade with our network.</p>
      <a class="btn">DOWNLOAD BROCHURE</a>
    </div>
  </div>
</section>

<section class="promise">
  <div class="promise-head">
    <svg width="40" height="36" viewBox="0 0 40 36"><path d="M20 34S3 23 3 12a8 8 0 0 1 17-3 8 8 0 0 1 17 3c0 11-17 22-17 22z" fill="none" stroke="#fff" stroke-width="2"/></svg>
    <h2>Our Promise</h2>
  </div>
  <blockquote>“A greener, more cost-efficient, and quality-driven supply chain through a collaborative life sciences marketplace.”</blockquote>
</section>

<footer class="site-footer">
  <div>
    <h4>QUICK LINKS</h4>
    <div class="footer-cols">
      <ul><li>Home</li><li>Why VerdaLink</li><li>About Us</li></ul>
      <ul><li>Our Partners</li><li>White Paper</li><li>Quality Policy</li></ul>
    </div>
  </div>
  <div>
    <h4>MY ACCOUNT</h4>
    <ul><li>Log in</li><li>Register</li></ul>
  </div>
  <div class="contact">
    <h4>CONTACT INFO</h4>
    <div class="contact-grid">
      <span>120 Linden Way</span><span>1 555 010 2468</span>
      <span>Harbor City, OH 44000</span><span>hello@verdalink.com</span>
    </div>
  </div>
</footer>
<div class="footer-bar">
  <span>© 2024 VerdaLink. All Rights Reserved</span>
  <div class="social"><span></span><span></span><span></span></div>
</div>

</body>
</html>
```